Top label sticker design -Australian Owned

We are seeking to develop a top sticker for our range of batteries, 80mm x 30mm.
Enclosed is the current top label sample, and new label will also be added. The message we want to send is, state that we are "100% Australian Family Owned", would like to use our Ostvane Logo merged with an Australian flag or similar to show the strength and roots of our brand.

Target Market(s)

30 to 50 year old males

Industry/Entity Type

Automotive

Requirements
Must have
• "100% Australian Family Owned" text or similar wording
Ostvane logo
Nice to have
• Blend of Australian flag with/ across our Ostvane logo.
Red background colour, Tellbrook Carriers Red.
Should not have
• To much much fluff, want to achieve a short sharp message.

```html
<!DOCTYPE html>
<html lang="en">
<head>
<meta charset="utf-8">
<title>Ostvane – Top Label Concepts</title>
<link href="https://fonts.googleapis.com/css2?family=Ubuntu:wght@400;500;700&display=swap" rel="stylesheet">
<style>
  :root {
    --stage: #111111;
    --label-red: #e2002b;
    --label-red-deep: #c8001f;
    --oval-white: #ffffff;
    --ink: #111111;
    --flag-navy: #012169;
    --flag-red: #e4002b;
    --flag-white: #ffffff;
    --tag-white: #ffffff;
    --mark-red: #c8141e;
  }
  * { box-sizing: border-box; margin: 0; padding: 0; }
  html, body {
    width: 1027px; height: 1200px; overflow: hidden;
    background: var(--stage);
    font-family: "Ubuntu", sans-serif;
  }
  .defs { position: absolute; width: 0; height: 0; overflow: hidden; }
  .canvas { position: relative; width: 1027px; height: 1200px; }
  .label {
    position: absolute; left: 77px; width: 874px; height: 328px;
    background: radial-gradient(ellipse at 50% 45%, var(--label-red) 55%, var(--label-red-deep) 100%);
    overflow: hidden;
  }
  .label--sweep { top: 56px; }
  .label--inset { top: 430px; }
  .label--badge { top: 804px; }
  .label__flag-sweep { position: absolute; inset: 0; width: 874px; height: 328px; }
  .oval {
    position: absolute; top: 77px; width: 438px; height: 175px;
    border-radius: 50%;
    background: var(--oval-white);
    box-shadow: 0 10px 28px rgba(120, 0, 20, 0.45);
    overflow: hidden;
  }
  .label--sweep .oval { left: 183px; }
  .label--inset .oval { left: 223px; width: 428px; height: 176px; }
  .label--badge .oval { left: 222px; width: 428px; height: 175px; }
  .brand { position: absolute; color: var(--ink); text-align: left; }
  .brand__name {
    display: block; font-weight: 500; font-size: 58px; line-height: 1;
    letter-spacing: -0.5px;
  }
  .brand__range {
    display: block; font-weight: 400; font-size: 17.5px; line-height: 1;
    margin-top: 2px; word-spacing: 7px; letter-spacing: 0.2px;
  }
  .label--sweep .brand { left: 106px; top: 26px; }
  .label--inset .brand { left: 70px; top: 32px; }
  .label--badge .brand { left: 111px; top: 27px; }
  .brand__dot {
    position: absolute; width: 30px; height: 30px; border-radius: 50%;
    background: var(--mark-red);
  }
  .label--sweep .brand__dot { left: 226px; top: 124px; }
  .label--inset .brand__dot { left: 196px; top: 128px; }
  .label--badge .brand__dot { left: 232px; top: 120px; }
  .oval__flag { position: absolute; left: 322px; top: 13px; width: 106px; height: 149px; }
  .oval__mini-flag { position: absolute; left: 110px; top: 118px; width: 64px; height: 32px; }
  .tagline {
    position: absolute; top: 277px; left: 0; width: 100%;
    color: var(--tag-white); font-weight: 700; font-size: 21.5px;
    letter-spacing: 0.3px; text-align: center; line-height: 26px;
  }
  .label--sweep .tagline { left: -42px; }
  .label--inset .tagline { left: 0px; }
  .label--badge .tagline { left: 5px; }
</style>
</head>
<body>
<svg class="defs" aria-hidden="true">
  <defs>
    <symbol id="star" viewBox="-1 -1 2 2">
      <polygon fill="var(--flag-white)" points="0,-1 0.191,-0.396 0.782,-0.623 0.429,-0.098 0.975,0.223 0.344,0.274 0.434,0.901 0,0.44 -0.434,0.901 -0.344,0.274 -0.975,0.223 -0.429,-0.098 -0.782,-0.623 -0.191,-0.396"/>
    </symbol>
    <clipPath id="canton-clip"><rect width="600" height="300"/></clipPath>
    <symbol id="aus-flag" viewBox="0 0 1200 600">
      <rect width="1200" height="600" fill="var(--flag-navy)"/>
      <g clip-path="url(#canton-clip)">
        <path d="M0 0 L600 300 M600 0 L0 300" stroke="var(--flag-white)" stroke-width="60"/>
        <path d="M0 0 L600 300 M600 0 L0 300" stroke="var(--flag-red)" stroke-width="20"/>
        <rect x="250" y="0" width="100" height="300" fill="var(--flag-white)"/>
        <rect x="0" y="100" width="600" height="100" fill="var(--flag-white)"/>
        <rect x="270" y="0" width="60" height="300" fill="var(--flag-red)"/>
        <rect x="0" y="120" width="600" height="60" fill="var(--flag-red)"/>
      </g>
      <use href="#star" x="210" y="360" width="180" height="180"/>
      <use href="#star" x="855" y="455" width="90" height="90"/>
      <use href="#star" x="855" y="55" width="90" height="90"/>
      <use href="#star" x="695" y="215" width="90" height="90"/>
      <use href="#star" x="985" y="185" width="90" height="90"/>
      <use href="#star" x="915" y="310" width="40" height="40"/>
    </symbol>
    <clipPath id="sweep-clip">
      <path d="M676 0 Q752 120 746 245 Q744 290 743 328 L874 328 L874 0 Z"/>
    </clipPath>
  </defs>
</svg>

<main class="canvas">

  <section class="label label--sweep">
    <svg class="label__flag-sweep" viewBox="0 0 874 328" role="img" aria-label="Australian flag sweeping in from the right edge">
      <g clip-path="url(#sweep-clip)">
        <rect x="600" y="0" width="274" height="328" fill="var(--flag-navy)"/>
        <use href="#aus-flag" x="637" y="-17" width="816" height="408"/>
        <use href="#star" x="676" y="58" width="44" height="44"/>
        <use href="#star" x="715" y="322" width="20" height="20"/>
      </g>
    </svg>
    <div class="oval">
      <div class="brand">
        <span class="brand__name">Ostvane</span>
        <span class="brand__range">BATTERIES OILS FILTERS</span>
      </div>
      <span class="brand__dot"></span>
    </div>
    <p class="tagline">100% Australian Family Owned</p>
  </section>

  <section class="label label--inset">
    <div class="oval">
      <div class="brand">
        <span class="brand__name">Ostvane</span>
        <span class="brand__range">BATTERIES OILS FILTERS</span>
      </div>
      <span class="brand__dot"></span>
      <svg class="oval__flag" viewBox="0 0 106 149" role="img" aria-label="Australian flag filling the right end of the oval">
        <rect width="106" height="149" fill="var(--flag-navy)"/>
        <use href="#aus-flag" x="0" y="0" width="212" height="106"/>
        <use href="#star" x="52" y="85" width="36" height="36"/>
      </svg>
    </div>
    <p class="tagline">100% Australian Family Owned</p>
  </section>

  <section class="label label--badge">
    <div class="oval">
      <div class="brand">
        <span class="brand__name">Ostvane</span>
        <span class="brand__range">BATTERIES OILS FILTERS</span>
      </div>
      <span class="brand__dot"></span>
      <svg class="oval__mini-flag" viewBox="0 0 1200 600" role="img" aria-label="Small Australian flag">
        <use href="#aus-flag" x="0" y="0" width="1200" height="600"/>
      </svg>
    </div>
    <p class="tagline">100% Australian Family Owned</p>
  </section>

</main>
</body>
</html>
```